Powerpoint Presentation Template

Kindly design a business class Powepoint Presentation template for our business use. Please stick to our company colours or even pictures as shown on our website and Logo

```html
<!DOCTYPE html>
<html lang="en">
<head>
<meta charset="utf-8">
<title>Kestrelane Properties – Presentation Template</title>
<link href="https://fonts.googleapis.com/css2?family=Anton&family=Open+Sans:wght@400;600;700&display=swap" rel="stylesheet">
<style>
:root{
  --red:#8b2326;
  --red-mid:#a5474a;
  --red-soft:#c07a7c;
  --grey:#5a5a5a;
  --grey-mid:#7a7a7a;
  --text:#555;
  --paper:#fff;
  --photo-dark:linear-gradient(135deg,#4a1a1b,#6b2e2c 50%,#2d1515);
  --photo-build:linear-gradient(160deg,#8d9aa6,#c9ced2 55%,#5c6168);
  --display:'Anton',sans-serif;
  --body:'Open Sans',sans-serif;
}
*{margin:0;padding:0;box-sizing:border-box}
html,body{width:1200px;height:1200px;overflow:hidden;background:var(--paper);font-family:var(--body);color:var(--text)}
.sheet{position:relative;width:1200px;height:1200px}
.slide{position:absolute;width:400px;height:225px;overflow:hidden;background:var(--paper)}
.abs{position:absolute}
.photo{position:absolute;background:var(--photo-dark)}
.photo.build{background:var(--photo-build)}
.brand{position:absolute;font-family:var(--display);color:var(--red);font-size:9px;line-height:1;text-align:right}
.brand span{display:block;font-family:var(--body);font-size:5.5px;color:var(--grey);margin-top:1px}
.heading{position:absolute;font-family:var(--display);color:var(--red);text-transform:uppercase;letter-spacing:.3px;line-height:1.15}
.lorem{position:absolute;font-size:5.6px;line-height:1.32;color:var(--text)}
.pill{position:absolute;background:var(--red);color:#fff;font-size:6px;font-weight:600;text-align:center;border-radius:8px;line-height:12px;height:12px}
.caption{position:absolute;left:34px;top:1148px;font-size:21px;color:#222;font-family:var(--body)}
</style>
</head>
<body>
<div class="sheet">

<!-- Cover -->
<section class="slide" style="left:0;top:0">
  <div class="abs" style="left:0;top:0;width:400px;height:20px;background:var(--red);color:#fff;font-size:6.5px;line-height:20px;padding:0 8px">Kestrelane Properties South Africa<span style="float:right;letter-spacing:.5px">www.kestrelane.com</span></div>
  <div class="photo" style="left:0;top:20px;width:216px;height:205px" role="img" aria-label="Dimmed photo of a modern office interior"></div>
  <svg class="abs" style="left:0;top:20px" width="216" height="205"><polygon points="40,0 156,0 156,175 40,192" fill="#8b2326" opacity=".85"/></svg>
  <div class="heading" style="left:51px;top:62px;color:#fff;font-size:21px;line-height:1.4;letter-spacing:1.5px">Your Title<br>Here</div>
  <div class="abs" style="left:51px;top:131px;color:#fff;font-size:7.5px">Your subtitle here</div>
  <div class="abs" style="right:28px;top:42px;text-align:right;font-size:7px;line-height:1.2;color:var(--grey);border-right:1px solid #ccc;padding-right:10px"><b>HEAD OFFICE</b><br>42 Marlow Avenue<br>Rosebank East,<br>Johannesburg, 2199<br><b>Tel:</b> +27 11 555 0142<br><b>Fax:</b> +27 11 555 0187</div>
  <div class="brand" style="right:16px;top:176px;font-size:20px">Kestrelane<span style="font-size:12px">Properties</span></div>
</section>

<!-- About us 1 -->
<section class="slide" style="left:400px;top:0">
  <div class="brand" style="left:10px;top:10px;text-align:left">Kestrelane<span>Properties</span></div>
  <div class="heading" style="right:22px;top:16px;font-size:20px">About Us</div>
  <div class="abs" style="left:0;top:50px;width:400px;height:92px;background:var(--red-mid)"></div>
  <div class="photo" style="left:21px;top:64px;width:104px;height:62px" role="img" aria-label="Photo of a reception area"></div>
  <div class="photo" style="left:146px;top:64px;width:104px;height:62px" role="img" aria-label="Photo of an office building exterior"></div>
  <div class="photo" style="left:272px;top:64px;width:104px;height:62px" role="img" aria-label="Photo of an interior hallway"></div>
  <p class="abs" style="right:22px;top:155px;width:240px;text-align:right;font-size:7.4px;line-height:1.3;color:#333"><b>Kestrelane Properties</b> is a leading 100% black owned South African housing and infrastructure development company. Our focus is the development of sustainable residential developments, civil and infrastructure development, as well as the construction of commercial facilities and buildings.</p>
</section>

<!-- About us 2 -->
<section class="slide" style="left:800px;top:0">
  <svg class="abs" style="left:0;top:0" width="400" height="225"><polygon points="400,35 400,225 210,225" fill="#8b2326" opacity=".85"/></svg>
  <div class="photo" style="left:268px;top:76px;width:108px;height:108px;border-radius:50%" role="img" aria-label="Round photo of a modern building"></div>
  <div class="brand" style="right:10px;top:10px">Kestrelane<span>Properties</span></div>
  <div class="heading" style="left:21px;top:18px;font-size:20px">About Us</div>
  <p class="lorem" style="left:21px;top:56px;width:250px;color:#222;font-size:5.4px">Our culture of <b>teamwork</b>, founded on the need for <b>collaboration and partnership</b>, guides our interaction with clients, and is the basis of <b>our approach to every construction project</b> we have successfully completed from our inception.</p>
  <div class="pill" style="left:21px;top:96px;width:78px;height:15px;line-height:15px;font-size:9px;font-weight:400">Our Vision</div>
  <div class="pill" style="left:142px;top:96px;width:78px;height:15px;line-height:15px;font-size:9px;font-weight:400">Our Mission</div>
  <p class="lorem" style="left:21px;top:121px;width:100px;font-size:5.2px">Our vision is to be a vibrant, self-driven organisation achieving distinction in the development of housing and infrastructure solutions. As a South African company, we aim to become the preferred supplier for projects related to social development and the economic wellbeing of our society.</p>
  <p class="lorem" style="left:145px;top:121px;width:100px;font-size:5.2px">Our mission is to develop significant partnerships with all our clients, business partners and beneficiaries. Kestrelane Properties provides top quality services with honesty, integrity and professionalism. We aim to participate in the creation of an environment that maximises sustainable growth of all stakeholders, provides affordable and sustainable housing and infrastructure, employment and wealth creation.</p>
</section>

<!-- Meet our team -->
<section class="slide" style="left:0;top:225px">
  <svg class="abs" style="left:0;top:0" width="400" height="225"><polygon points="400,20 400,225 238,225" fill="#5a5a5a"/></svg>
  <div class="heading" style="left:22px;top:20px;font-size:20px">Meet Our Team</div>
  <div class="brand" style="right:18px;top:12px">Kestrelane<span>Properties</span></div>
  <svg class="abs" style="left:0;top:50px" width="400" height="80" fill="#fff" stroke="#8b2326" stroke-width="1">
    <polygon points="80,2 86,7 74,7"/><rect x="33" y="7" width="83" height="83"/><polyline points="116,28 131,43 116,58" fill="none"/>
    <polyline points="183,7 198,-7 214,7" fill="none"/><rect x="158" y="7" width="83" height="83"/><polyline points="241,40 244,43 241,46" fill="none"/>
    <polyline points="298,7 307,-3 316,7" fill="none"/><rect x="283" y="7" width="82" height="83"/><polyline points="283,25 263,45 283,63" fill="none"/>
  </svg>
  <div class="pill" style="left:38px;top:153px;width:74px">Name here</div>
  <div class="pill" style="left:163px;top:153px;width:74px">Name here</div>
  <div class="pill" style="left:286px;top:153px;width:74px">Name here</div>
  <p class="lorem" style="left:30px;top:175px;width:90px;text-align:center">Lorem ipsum dolor sit amet, sonet postulant suavitate eu mel. Et eos vocent detraxit. Volutpat interesset in duo, per volumus albucius cu.</p>
  <p class="lorem" style="left:155px;top:175px;width:90px;text-align:center">Lorem ipsum dolor sit amet, sonet postulant suavitate eu mel. Et eos vocent detraxit. Volutpat interesset in duo, per volumus albucius cu.</p>
  <p class="lorem" style="left:278px;top:175px;width:90px;text-align:center;color:#eee">Lorem ipsum dolor sit amet, sonet postulant suavitate eu mel. Et eos vocent detraxit. Volutpat interesset in duo, per volumus albucius cu.</p>
</section>

<!-- Our services -->
<section class="slide" style="left:400px;top:225px">
  <svg class="abs" style="left:0;top:0" width="400" height="225"><polygon points="0,0 54,0 278,225 80,225 0,120" fill="#8b2326" opacity=".9"/></svg>
  <div class="heading" style="left:150px;top:16px;font-size:20px">Our Services</div>
  <div class="abs" style="left:230px;top:40px;width:26px;height:2px;background:var(--red)"></div>
  <div class="brand" style="right:18px;top:12px">Kestrelane<span>Properties</span></div>
  <svg class="abs" style="left:0;top:40px" width="400" height="80" fill="none" stroke="#8b2326" stroke-width=".8">
    <polygon points="82,32 102,10 122,32 102,54"/><polygon points="199,32 219,10 239,32 219,54"/><polygon points="316,32 336,10 356,32 336,54"/>
  </svg>
  <div class="photo" style="left:49px;top:54px;width:68px;height:68px" role="img" aria-label="Photo of a multi-storey building under construction"></div>
  <div class="photo" style="left:166px;top:54px;width:68px;height:68px" role="img" aria-label="Photo of road construction works"></div>
  <div class="photo" style="left:283px;top:54px;width:68px;height:68px" role="img" aria-label="Photo of a property development site"></div>
  <div class="pill" style="left:48px;top:131px;width:70px;font-size:5.6px">Building Construction</div>
  <div class="pill" style="left:156px;top:131px;width:88px;font-size:5.6px">Road &amp; Civil Construction</div>
  <div class="pill" style="left:279px;top:131px;width:76px;font-size:5.6px">Property Development</div>
  <p class="lorem" style="left:36px;top:150px;width:94px;height:52px;text-align:center;background:rgba(192,122,124,.55);color:#fff;font-size:5.1px;padding:1px">Kestrelane Properties has over 16 years' experience in building construction in South Africa. Over the years we have successfully completed building construction projects for public and private sector clients.</p>
  <p class="lorem" style="left:152px;top:150px;width:96px;height:58px;text-align:center;background:rgba(216,170,172,.85);color:#444;font-size:5.1px;padding:1px">Kestrelane Properties has extensive experience in the provision of turnkey solutions for varied civil construction projects. Using our own plant equipment, we continue to deliver on Roads and Earthworks, Water and Sanitation.</p>
  <p class="lorem" style="left:272px;top:150px;width:90px;text-align:center;font-size:5.1px">Kestrelane Properties works in tandem with Vantora, a Kestrelane Group company, in the development of real estate infrastructure throughout South Africa.</p>
</section>

<!-- Title text 1 -->
<section class="slide" style="left:800px;top:225px">
  <svg class="abs" style="left:0;top:0" width="400" height="225"><polygon points="0,0 110,0 181,225 0,225" fill="#8b2326" opacity=".95"/></svg>
  <div class="photo" style="left:50px;top:65px;width:155px;height:94px;opacity:.8" role="img" aria-label="Photo of an office interior with large windows"></div>
  <div class="brand" style="right:10px;top:12px">Kestrelane<span>Properties</span></div>
  <div class="heading" style="left:225px;top:28px;font-size:21px;color:#111;line-height:1.5">Title Text<br>Here</div>
  <div class="abs" style="left:224px;top:92px;width:1px;height:96px;background:#ccc"></div>
  <p class="lorem" style="left:232px;top:92px;width:130px">Lorem ipsum dolor sit amet, sonet postulant suavitate eu mel. Et eos vocent detraxit. Volutpat interesset in duo, per volumus albucius cu. Sea nonumy altera epicurei cu, mea id nulla dolorum civibus.<br><br>Est ad dicunt feugiat consulatu. Fastidii referrentur qui ut. An sea mucius adolescens. Minim constituam ne has, has nullam antiopam no.</p>
</section>

<!-- Title text 2 -->
<section class="slide" style="left:0;top:450px">
  <svg class="abs" style="left:0;top:0" width="400" height="225"><polygon points="223,0 400,0 400,225 307,225" fill="#7a7a7a"/></svg>
  <div class="photo build" style="left:192px;top:64px;width:158px;height:95px" role="img" aria-label="Photo of a row of white modern townhouses"></div>
  <div class="brand" style="left:10px;top:12px;text-align:left">Kestrelane<span>Properties</span></div>
  <div class="heading" style="right:238px;top:28px;font-size:21px;line-height:1.5;text-align:right">Title Text<br>Here</div>
  <p class="lorem" style="right:238px;top:92px;width:120px;text-align:right">Lorem ipsum dolor sit amet, sonet postulant suavitate eu mel. Et eos vocent detraxit. Volutpat interesset in duo, per volumus albucius cu. Sea nonumy altera epicurei cu, mea id nulla dolorum civibus.<br><br>Est ad dicunt feugiat consulatu. Fastidii referrentur qui ut. An sea mucius adolescens. Minim constituam ne has, has nullam antiopam no.</p>
  <div class="abs" style="left:168px;top:92px;width:1px;height:96px;background:#ccc"></div>
</section>

<!-- Title text 3 -->
<section class="slide" style="left:400px;top:450px">
  <div class="brand" style="left:10px;top:12px;text-align:left">Kestrelane<span>Properties</span></div>
  <div class="abs" style="left:63px;top:0;width:80px;height:110px;background:var(--red-soft)"></div>
  <svg class="abs" style="left:25px;top:36px" width="150" height="160"><circle cx="82" cy="88" r="55" fill="none" stroke="#8b2326" stroke-width="1.2"/></svg>
  <div class="photo" style="left:29px;top:38px;width:104px;height:104px;border-radius:50%;opacity:.9" role="img" aria-label="Round photo of a building facade"></div>
  <div class="photo" style="left:58px;top:63px;width:100px;height:100px;border-radius:50%;opacity:.85" role="img" aria-label="Round photo of a building facade detail"></div>
  <div class="heading" style="right:34px;top:24px;font-size:21px;line-height:1.5;color:#111;text-align:right">Title Text<br>Here</div>
  <p class="lorem" style="right:42px;top:88px;width:140px;text-align:right">Lorem ipsum dolor sit amet, sonet postulant suavitate eu mel. Et eos vocent detraxit. Volutpat interesset in duo, per volumus albucius cu. Sea nonumy altera epicurei cu, mea id nulla dolorum civibus.<br><br>Est ad dicunt feugiat consulatu. Fastidii referrentur qui ut. An sea mucius adolescens. Minim constituam ne has, has nullam antiopam no.</p>
  <div class="abs" style="right:34px;top:88px;width:1px;height:96px;background:#ccc"></div>
  <div class="abs" style="left:0;top:212px;width:400px;height:13px;background:var(--red)"></div>
</section>

<!-- Gallery -->
<section class="slide" style="left:800px;top:450px">
  <div class="abs" style="left:0;top:0;width:116px;height:225px;background:var(--red-mid)"></div>
  <div class="heading" style="left:6px;top:20px;font-size:21px;color:#fff;line-height:1.55;letter-spacing:.6px">Our<br>Gallery</div>
  <div class="abs" style="left:70px;top:83px;width:22px;height:2px;background:#fff"></div>
  <div class="abs" style="left:12px;top:198px;color:#fff;font-size:6px;letter-spacing:.5px;line-height:1.4">For more, visit:<br>www.kestrelane.com</div>
  <div class="photo build" style="left:125px;top:13px;width:83px;height:49px" role="img" aria-label="Photo of a construction site"></div>
  <div class="photo build" style="left:216px;top:13px;width:83px;height:49px" role="img" aria-label="Photo of a modern house with pool"></div>
  <div class="photo" style="left:308px;top:13px;width:83px;height:49px" role="img" aria-label="Photo of an interior corridor"></div>
  <div class="photo" style="left:125px;top:73px;width:83px;height:49px" role="img" aria-label="Photo of an office interior"></div>
  <div class="photo" style="left:216px;top:73px;width:83px;height:49px" role="img" aria-label="Photo of a stairwell"></div>
  <div class="photo build" style="left:308px;top:73px;width:83px;height:49px" role="img" aria-label="Photo of a lounge area"></div>
  <div class="photo build" style="left:125px;top:133px;width:83px;height:49px" role="img" aria-label="Photo of white townhouses"></div>
  <div class="photo build" style="left:216px;top:133px;width:83px;height:49px" role="img" aria-label="Photo of a building with a steel roof"></div>
  <div class="photo build" style="left:308px;top:133px;width:83px;height:49px" role="img" aria-label="Photo of road paving works"></div>
  <div class="brand" style="right:7px;top:202px">Kestrelane<span>Properties</span></div>
</section>

<!-- Bullet point slide -->
<section class="slide" style="left:0;top:675px">
  <div class="heading" style="left:130px;top:20px;font-size:19px">Bullet Point Slide</div>
  <div class="brand" style="right:14px;top:10px">Kestrelane<span>Properties</span></div>
  <div class="abs" style="left:133px;top:56px;width:132px;height:153px;background:var(--grey)"></div>
  <div class="abs" style="left:47px;top:73px;width:44px;height:17px;border-radius:9px;background:var(--red-soft)"></div>
  <div class="abs" style="left:177px;top:73px;width:44px;height:17px;border-radius:9px;background:var(--red-soft)"></div>
  <div class="abs" style="left:308px;top:73px;width:44px;height:17px;border-radius:9px;background:var(--red-soft)"></div>
  <div class="heading" style="left:47px;top:59px;width:44px;text-align:center;font-size:18px">1</div>
  <div class="heading" style="left:177px;top:59px;width:44px;text-align:center;font-size:18px;color:#fff">2</div>
  <div class="heading" style="left:308px;top:59px;width:44px;text-align:center;font-size:18px">3</div>
  <p class="lorem" style="left:18px;top:101px;width:102px;text-align:center">Lorem ipsum dolor sit amet, sonet postulant suavitate eu mel. Et eos vocent detraxit. Volutpat interesset in duo, per volumus albucius cu. Sea nonumy altera epicurei cu, mea id nulla dolorum civibus.<br><br>Est ad dicunt feugiat consulatu. Fastidii referrentur qui ut. An sea mucius adolescens. Minim constituam ne has, has nullam antiopam no.</p>
  <p class="lorem" style="left:148px;top:101px;width:102px;text-align:center;color:#eee">Lorem ipsum dolor sit amet, sonet postulant suavitate eu mel. Et eos vocent detraxit. Volutpat interesset in duo, per volumus albucius cu. Sea nonumy altera epicurei cu, mea id nulla dolorum civibus.<br><br>Est ad dicunt feugiat consulatu. Fastidii referrentur qui ut. An sea mucius adolescens. Minim constituam ne has, has nullam antiopam no.</p>
  <p class="lorem" style="left:279px;top:101px;width:102px;text-align:center">Lorem ipsum dolor sit amet, sonet postulant suavitate eu mel. Et eos vocent detraxit. Volutpat interesset in duo, per volumus albucius cu. Sea nonumy altera epicurei cu, mea id nulla dolorum civibus.<br><br>Est ad dicunt feugiat consulatu. Fastidii referrentur qui ut. An sea mucius adolescens. Minim constituam ne has, has nullam antiopam no.</p>
</section>

<!-- Steps slide -->
<section class="slide" style="left:400px;top:675px">
  <div class="abs" style="left:142px;top:0;width:116px;height:225px;background:var(--red-mid)"></div>
  <div class="heading" style="left:142px;top:26px;width:116px;text-align:center;font-size:18px;color:#fff">Steps Slide</div>
  <div class="brand" style="right:14px;top:10px">Kestrelane<span>Properties</span></div>
  <svg class="abs" style="left:0;top:80px" width="400" height="20"><line x1="62" y1="7" x2="337" y2="7" stroke="#8b2326" stroke-width="1.5"/><circle cx="62" cy="7" r="6" fill="#5a5a5a"/><circle cx="199" cy="7" r="6" fill="#5a5a5a"/><circle cx="337" cy="7" r="6" fill="#5a5a5a"/></svg>
  <div class="pill" style="left:43px;top:108px;width:38px">Name</div>
  <div class="pill" style="left:180px;top:108px;width:38px">Name</div>
  <div class="pill" style="left:318px;top:108px;width:38px">Name</div>
  <p class="lorem" style="left:20px;top:123px;width:84px;text-align:center">Lorem ipsum dolor sit amet, sonet postulant suavitate eu mel. Et eos vocent detraxit. Volutpat interesset in duo, per volumus albucius cu. Sea nonumy altera epicurei cu, mea id nulla dolorum civibus.</p>
  <p class="lorem" style="left:157px;top:123px;width:86px;text-align:center;color:#eee">Lorem ipsum dolor sit amet, sonet postulant suavitate eu mel. Et eos vocent detraxit. Volutpat interesset in duo, per volumus albucius cu. Sea nonumy altera epicurei cu, mea id nulla dolorum civibus.</p>
  <p class="lorem" style="left:295px;top:123px;width:84px;text-align:center">Lorem ipsum dolor sit amet, sonet postulant suavitate eu mel. Et eos vocent detraxit. Volutpat interesset in duo, per volumus albucius cu. Sea nonumy altera epicurei cu, mea id nulla dolorum civibus.</p>
</section>

<!-- Map slide -->
<section class="slide" style="left:800px;top:675px">
  <div class="brand" style="left:12px;top:10px;text-align:left">Kestrelane<span>Properties</span></div>
  <div class="heading" style="right:22px;top:20px;font-size:17px">Title Here</div>
  <div class="abs" style="left:108px;top:52px;width:268px;height:152px;border-radius:40px;background:radial-gradient(ellipse at center,#8b2326 40%,rgba(139,35,38,.75) 75%,rgba(255,255,255,0) 100%)" role="img" aria-label="World map with location markers"></div>
  <svg class="abs" style="left:29px;top:79px" width="30" height="42"><path d="M15 2a12 12 0 0 1 12 12c0 9-12 26-12 26S3 23 3 14A12 12 0 0 1 15 2z" fill="#bdbdbd"/><circle cx="15" cy="14" r="5" fill="#fff"/></svg>
  <div class="pill" style="left:24px;top:122px;width:40px">Name</div>
  <p class="lorem" style="left:24px;top:139px;width:74px;text-align:justify">Lorem ipsum dolor sit amet, sonet postulant suavitate eu mel. Et eos vocent detraxit. Volutpat interesset in duo, per volumus albucius cu. Sea nonumy altera epicurei cu, mea id nulla dolorum civibus.</p>
</section>

<!-- Bar chart slide -->
<section class="slide" style="left:0;top:900px">
  <div class="abs" style="left:0;top:0;width:16px;height:225px;background:var(--red)"></div>
  <div class="photo" style="left:16px;top:0;width:124px;height:225px" role="img" aria-label="Dimmed photo of a building interior"></div>
  <p class="lorem" style="left:32px;top:12px;width:84px;color:#eee">Lorem ipsum dolor sit amet, sonet postulant suavitate eu mel. Et eos vocent detraxit. Volutpat interesset in duo, per volumus albucius cu. Sea nonumy altera epicurei cu, mea id nulla dolorum civibus.</p>
  <div class="heading" style="right:17px;top:11px;font-size:15px">SmartArt Slide</div>
  <svg class="abs" style="left:160px;top:60px" width="230" height="140" font-family="Open Sans, sans-serif" font-size="5" fill="#777">
    <text x="113" y="4" font-size="6.5" text-anchor="middle">Chart Title</text>
    <g stroke="#e2e2e2" stroke-width=".5"><line x1="12" y1="15" x2="218" y2="15"/><line x1="12" y1="32" x2="218" y2="32"/><line x1="12" y1="50" x2="218" y2="50"/><line x1="12" y1="67" x2="218" y2="67"/><line x1="12" y1="84" x2="218" y2="84"/><line x1="12" y1="101" x2="218" y2="101"/><line x1="12" y1="119" x2="218" y2="119"/></g>
    <g text-anchor="end"><text x="8" y="17">6</text><text x="8" y="34">5</text><text x="8" y="52">4</text><text x="8" y="69">3</text><text x="8" y="86">2</text><text x="8" y="103">1</text><text x="8" y="121">0</text></g>
    <g fill="#8b2326"><rect x="25" y="44.5" width="8" height="74.5"/><rect x="76" y="75.5" width="8" height="43.5"/><rect x="126" y="58.5" width="8" height="60.5"/><rect x="177" y="41" width="8" height="78"/></g>
    <g fill="#a5474a"><rect x="36" y="77.5" width="8" height="41.5"/><rect x="87" y="43" width="8" height="76"/><rect x="137" y="88" width="8" height="31"/><rect x="188" y="70.5" width="8" height="48.5"/></g>
    <g fill="#b5585b"><rect x="47" y="84.5" width="8" height="34.5"/><rect x="98" y="84.5" width="8" height="34.5"/><rect x="148" y="67" width="8" height="52"/><rect x="199" y="32.5" width="8" height="86.5"/></g>
    <g text-anchor="middle"><text x="40" y="128">Category 1</text><text x="91" y="128">Category 2</text><text x="141" y="128">Category 3</text><text x="192" y="128">Category 4</text></g>
    <rect x="75" y="133" width="3" height="3" fill="#8b2326"/><text x="80" y="136">Series 1</text>
    <rect x="102" y="133" width="3" height="3" fill="#a5474a"/><text x="107" y="136">Series 2</text>
    <rect x="129" y="133" width="3" height="3" fill="#b5585b"/><text x="134" y="136">Series 3</text>
  </svg>
</section>

<!-- Bullet point slide 2 -->
<section class="slide" style="left:400px;top:900px">
  <div class="brand" style="left:10px;top:6px;text-align:left">Kestrelane<span>Properties</span></div>
  <div class="heading" style="right:22px;top:14px;font-size:15px">Bullet Point Slide</div>
  <div class="abs" style="left:322px;top:34px;width:18px;height:2px;background:var(--red)"></div>
  <svg class="abs" style="left:0;top:54px" width="400" height="46"><circle cx="64" cy="22" r="21" fill="#8b2326"/><circle cx="154" cy="22" r="21" fill="#5a5a5a"/><circle cx="244" cy="22" r="21" fill="#8b2326"/><circle cx="334" cy="22" r="21" fill="#5a5a5a"/></svg>
  <div class="abs" style="left:24px;top:110px;width:80px;text-align:center;font-size:6px;font-weight:700;color:#222">Name of the stuff</div>
  <div class="abs" style="left:114px;top:110px;width:80px;text-align:center;font-size:6px;font-weight:700;color:#222">Name of the stuff</div>
  <div class="abs" style="left:204px;top:110px;width:80px;text-align:center;font-size:6px;font-weight:700;color:#222">Name of the stuff</div>
  <div class="abs" style="left:294px;top:110px;width:80px;text-align:center;font-size:6px;font-weight:700;color:#222">Name of the stuff</div>
  <p class="lorem" style="left:28px;top:127px;width:74px;text-align:justify">Lorem ipsum dolor sit amet, sonet postulant suavitate eu mel. Et eos vocent detraxit. Volutpat interesset in duo, per volumus albucius cu. Sea nonumy altera epicurei cu, mea id nulla dolorum civibus.</p>
  <p class="lorem" style="left:118px;top:127px;width:74px;text-align:justify">Lorem ipsum dolor sit amet, sonet postulant suavitate eu mel. Et eos vocent detraxit. Volutpat interesset in duo, per volumus albucius cu. Sea nonumy altera epicurei cu, mea id nulla dolorum civibus.</p>
  <p class="lorem" style="left:208px;top:127px;width:74px;text-align:justify">Lorem ipsum dolor sit amet, sonet postulant suavitate eu mel. Et eos vocent detraxit. Volutpat interesset in duo, per volumus albucius cu. Sea nonumy altera epicurei cu, mea id nulla dolorum civibus.</p>
  <p class="lorem" style="left:298px;top:127px;width:74px;text-align:justify">Lorem ipsum dolor sit amet, sonet postulant suavitate eu mel. Et eos vocent detraxit. Volutpat interesset in duo, per volumus albucius cu. Sea nonumy altera epicurei cu, mea id nulla dolorum civibus.</p>
</section>

<!-- Donut chart slide -->
<section class="slide" style="left:800px;top:900px">
  <div class="abs" style="left:0;top:0;width:16px;height:225px;background:var(--red)"></div>
  <div class="photo" style="left:16px;top:0;width:124px;height:225px" role="img" aria-label="Dimmed photo of a building interior"></div>
  <p class="lorem" style="left:32px;top:12px;width:84px;color:#eee">Lorem ipsum dolor sit amet, sonet postulant suavitate eu mel. Et eos vocent detraxit. Volutpat interesset in duo, per volumus albucius cu. Sea nonumy altera epicurei cu, mea id nulla dolorum civibus.</p>
  <div class="heading" style="right:17px;top:11px;font-size:15px">SmartArt Slide</div>
  <div class="abs" style="left:236px;top:30px;width:60px;text-align:center;font-size:9px;color:#555">Sales</div>
  <svg class="abs" style="left:196px;top:46px" width="140" height="140" viewBox="0 0 140 140">
    <g transform="rotate(-90 70 70)" fill="none" stroke-width="13">
      <circle cx="70" cy="70" r="58" stroke="#a5474a" stroke-dasharray="214 150.4"/>
      <circle cx="70" cy="70" r="58" stroke="#8b2326" stroke-dasharray="0 214 91 59.4"/>
      <circle cx="70" cy="70" r="58" stroke="#7d1f22" stroke-dasharray="0 305 36 23.4"/>
      <circle cx="70" cy="70" r="58" stroke="#b86466" stroke-dasharray="0 341 23.4 0"/>
    </g>
    <g stroke="#fff" stroke-width="1"><line x1="70" y1="5" x2="70" y2="19"/></g>
  </svg>
  <svg class="abs" style="left:216px;top:192px" width="110" height="8" font-family="Open Sans, sans-serif" font-size="4.5" fill="#777">
    <rect x="2" y="2" width="3" height="3" fill="#a5474a"/><text x="7" y="5">1st Qtr</text>
    <rect x="28" y="2" width="3" height="3" fill="#8b2326"/><text x="33" y="5">2nd Qtr</text>
    <rect x="55" y="2" width="3" height="3" fill="#7d1f22"/><text x="60" y="5">3rd Qtr</text>
    <rect x="82" y="2" width="3" height="3" fill="#b86466"/><text x="87" y="5">4th Qtr</text>
  </svg>
</section>

<div class="caption">Kestrelane PowerPoint Preview</div>
</div>
</body>
</html>
```